Promotional Flyer/Email Design - Cabling services for Broadcast and Audio Visual

We need a promotional flyer/email design to help launch our company, Velcor Lane. We provide cabling services for Broadcast Television and Audio Visual systems. Recent projects include major television events such as the Harrowmere Racquet Classic and Audio Visual/Entertainment systems for wealthy clients in their homes and on-board super yachts.

The flyer will be printed as single sided A5 and also be sent out in the body of a promotional email. It should feature the company logo along with a complementary colour scheme. It should have a clean finish with images that show the type of work we do (cabling and equipment installation) or the setting for these systems (tv studio, super yacht, cinema room, meeting room with projector etc.)

Services we offer are:

Broadcast/AV system design
On-site installation
Rack building
Pre-fabricated cable looms
Fibre optic installation

About the company:

Velcor Lane provide cabling services for Broadcast Television and Audio Visual systems. With over 15 years experience working in these industries we can help with every aspect of design, project managment, installation and maintenance. Our projects range from fibre optic cabling at major sports events to installing and commisioning bespoke control systems on some of the worlds largest super yachts.

Contact details:

To get a quote or discuss your project contact us now
Telephone: TBC
Email: info@velcor-lane.com
Website: www.velcor-lane.com
Address: TBC

Other information:

The company is based in London, UK. Our projects often take place in other countries with work taking place accross Europe and beyond.

We have a London based workshop for rack building and cable pre-fabrication.

Our website is www.velcor-lane.com

Images:

Images attached can be editted for use on the flyer or have ideas taken from them. Only the company logo is required to feature on the final design.

Target Market(s)

Business to business

Industry/Entity Type

It Company

Font styles to use
Sans Serif

Requirements
Must have
• Company logo
• List of services
• Contact details
Nice to have
• Image of cabling, home cinema room, super yacht, luxury home, outside broadcast truck, fibre optic equipment or cabling.

```html
<!DOCTYPE html>
<html lang="en">
<head>
<meta charset="utf-8">
<title>Velcor Lane – Cabling services flyer</title>
<link rel="stylesheet" href="https://fonts.googleapis.com/css2?family=PT+Sans:wght@400;700&family=Open+Sans:wght@300;400;700&display=swap">
<style>
  :root {
    --page-black: #000000;
    --paper: #ffffff;
    --headline-yellow: #f6e51c;
    --service-red: #e31b40;
    --about-blue: #3f7cc1;
    --logo-panel: #efeff2;
    --contact-dark: #2c2c2e;
    --ink-dark: #333333;
    --text-white: #ffffff;
  }
  * { box-sizing: border-box; margin: 0; padding: 0; }
  html, body { width: 866px; height: 1200px; overflow: hidden; background: var(--paper); }
  body { position: relative; font-family: "PT Sans", "Open Sans", sans-serif; }

  .flyer { position: absolute; left: 18px; top: 18px; width: 829px; height: 1163px; background: var(--page-black); overflow: hidden; }
  .abs { position: absolute; }

  .hero-photo { left: 0; top: 0; width: 829px; height: 464px;
    background: radial-gradient(ellipse at 62% 38%, #d8d2c6 0%, #9a8e7c 28%, #5e5446 60%, #3a3128 100%); }
  .headline { left: 32px; top: 62px; width: 300px; color: var(--headline-yellow);
    font-family: "Open Sans", sans-serif; font-weight: 700; font-size: 37px; line-height: 48px;
    letter-spacing: -0.3px; text-shadow: 2px 2px 4px rgba(0,0,0,0.6); }

  .services { left: 17px; top: 479px; width: 366px; height: 240px; background: var(--service-red); overflow: hidden; color: var(--text-white); }
  .services h2 { position: absolute; left: 39px; top: 10px; font-family: "Open Sans", sans-serif; font-weight: 300; font-size: 35px; }
  .services ul { position: absolute; left: 40px; top: 69px; list-style: none; white-space: nowrap; }
  .services li { position: relative; padding-left: 28px; font-family: "Open Sans", sans-serif; font-weight: 700; font-size: 19px; line-height: 32.5px; }
  .services li::before { content: ""; position: absolute; left: 0; top: 9px; width: 14px; height: 14px; border-radius: 50%;
    background: #111; box-shadow: 0 0 0 1.5px #fff; }

  .about { left: 392px; top: 479px; width: 416px; height: 240px; background: var(--about-blue); color: var(--text-white); }
  .about h2 { position: absolute; left: 18px; top: 15px; font-weight: 700; font-size: 22px; font-family: "Open Sans", sans-serif; }
  .about p { position: absolute; left: 18px; top: 64px; width: 372px; font-size: 14.3px; line-height: 20.9px; text-align: justify; }

  .brand { left: 17px; top: 725px; width: 366px; height: 231px; background: var(--logo-panel);
    display: flex; align-items: center; justify-content: center; gap: 14px; }
  .brand-dot { width: 26px; height: 26px; border-radius: 50%; background: var(--service-red); }
  .brand-name { font-family: "Open Sans", sans-serif; font-weight: 700; font-size: 44px; color: var(--ink-dark); letter-spacing: -1px; }

  .contact { left: 391px; top: 725px; width: 421px; height: 231px;
    background: linear-gradient(90deg, #1e1e20 0%, var(--contact-dark) 40%, var(--contact-dark) 100%);
    color: var(--text-white); text-align: center; }
  .contact-lead { position: absolute; left: 0; right: 0; top: 10px; font-size: 23px; line-height: 30px; }
  .contact-phone { position: absolute; left: 0; right: 0; top: 100px; color: var(--service-red);
    font-family: "Open Sans", sans-serif; font-weight: 700; font-size: 46px; line-height: 50px; letter-spacing: -0.5px; }
  .contact-email { position: absolute; left: 0; right: 0; top: 160px; font-family: "Open Sans", sans-serif; font-size: 19px; }
  .contact-web { position: absolute; left: 0; right: 0; top: 189px; font-family: "Open Sans", sans-serif; font-weight: 700; font-size: 21px; }

  .location-note { left: 0; top: 962px; width: 829px; text-align: center; color: var(--text-white);
    font-family: "Open Sans", sans-serif; font-size: 11.6px; line-height: 16px; }

  .gallery-item { top: 998px; height: 165px; }
  .photo-lounge { left: 0; width: 252px; background: linear-gradient(135deg, #8a7a63, #c9b99e 50%, #6b5a45); }
  .photo-studio { left: 260px; width: 272px; background: linear-gradient(180deg, #4a4a50, #bfc3c8 55%, #8e9096); }
  .photo-rack { left: 540px; width: 144px; background: linear-gradient(90deg, #b7b9bc, #3a3b3e 60%, #1c1c1e); }
  .photo-wiring { left: 688px; width: 141px; background: linear-gradient(160deg, #2a3a33, #4f6b5a 50%, #1a1f1c); }
</style>
</head>
<body>
<main class="flyer">
  <div class="abs hero-photo" role="img" aria-label="Home cinema room with large projection screen, curtains and reclining seats"></div>
  <h1 class="abs headline">Cabling services for Broadcast Television and Audio Visual systems</h1>

  <section class="abs services">
    <h2>Services:</h2>
    <ul>
      <li>Broadcast/AV system design</li>
      <li>On-site installation</li>
      <li>Rack building</li>
      <li>Pre-fabricated cable looms</li>
      <li>Fibre optic installation</li>
    </ul>
  </section>

  <section class="abs about">
    <h2>About the company:</h2>
    <p>Velcor Lane provide cabling services for Broadcast Television and Audio Visual systems. With over 15 years experience working in these industries we can help with every aspect of design, project managment, installation and maintenance. Our projects range from fibre optic cabling at major sports events to installing and commisioning bespoke control systems on some of the worlds largest super yachts.</p>
  </section>

  <div class="abs brand">
    <span class="brand-dot"></span>
    <span class="brand-name">Velcor Lane</span>
  </div>

  <section class="abs contact">
    <p class="contact-lead">To get a quote or discuss your<br>project Contact us now</p>
    <p class="contact-phone">07700 900 418</p>
    <p class="contact-email">info@velcor-lane.com</p>
    <p class="contact-web">www.velcor-lane.com</p>
  </section>

  <p class="abs location-note">The company is based in London, UK. Our projects often take place in other countries with work taking place accross Europe<br>and beyond. &nbsp;&nbsp;We have a London based workshop for rack building and cable pre-fabrication.</p>

  <div class="abs gallery-item photo-lounge" role="img" aria-label="Luxury living room with wall-mounted television"></div>
  <div class="abs gallery-item photo-studio" role="img" aria-label="Television studio floor with lighting rig and colour bars"></div>
  <div class="abs gallery-item photo-rack" role="img" aria-label="Equipment rack with patch panels and cabling"></div>
  <div class="abs gallery-item photo-wiring" role="img" aria-label="Open rack showing neatly dressed coloured cables"></div>
</main>
</body>
</html>
```